Business Card for Brevikpartners

Need to design a business card with attached logo

Target Market(s)

I'm a financial/Investment adviser so card must be professional

Industry/Entity Type

Business

Font styles to use
Serif
Sans Serif

Requirements
Must have
• Would like in include the GOLD version of my logo if possible

Teodor Brevik
President

Address is
4278 Pemberly Ave
San Ramon, Ca. 94617

Phone
510-647-3920
Fax
925-413-7782

Email
teodor@brevikpartners.example

I also need the following tag line at the bottom of card:

Investment Advisor Representative of and Securities offered
through Harwick Capital Brokerage, LLC Member NTVQA, OLBR
and Registered Investment Advisor.

Nice to have
• Split color in order to incorporate GOLD LOGO
Should not have

```html
<!DOCTYPE html>
<html lang="en">
<head>
<meta charset="utf-8">
<title>Brevik Partners — Business Card</title>
<link rel="stylesheet" href="https://fonts.googleapis.com/css2?family=Tinos:wght@400;700&display=swap">
<style>
  :root {
    --backdrop: #aaacb6;
    --card: #3b3b3c;
    --gold: #c49a4a;
    --white: #f1efe9;
    --card-w: 620px;
    --card-h: 354px;
  }
  * { box-sizing: border-box; margin: 0; padding: 0; }
  html, body {
    width: 1200px;
    height: 900px;
    overflow: hidden;
    background: var(--backdrop);
    font-family: "Tinos", "Times New Roman", serif;
  }
  .stage {
    width: 1200px;
    height: 900px;
    display: flex;
    flex-direction: column;
    align-items: center;
    justify-content: center;
    gap: 60px;
  }
  .card {
    position: relative;
    width: var(--card-w);
    height: var(--card-h);
    background: var(--card);
    box-shadow: 0 10px 24px rgba(40, 42, 52, 0.35);
  }

  /* Brand mark stand-in */
  .brand {
    display: flex;
    align-items: center;
    gap: 10px;
    color: var(--gold);
    font-weight: 400;
    text-transform: uppercase;
    letter-spacing: 0.06em;
  }
  .brand-dot {
    border-radius: 50%;
    background: var(--gold);
    flex: none;
  }

  /* Back */
  .card-back {
    display: flex;
    align-items: center;
    justify-content: center;
  }
  .card-back .brand { font-size: 30px; gap: 16px; }
  .card-back .brand-dot { width: 40px; height: 40px; }

  /* Front */
  .card-front .brand {
    position: absolute;
    left: 34px;
    top: 34px;
    font-size: 15px;
  }
  .card-front .brand-dot { width: 22px; height: 22px; }

  .divider {
    position: absolute;
    left: 53%;
    top: 0;
    width: 1.5px;
    height: 100%;
    background: var(--gold);
  }
  .identity {
    position: absolute;
    left: 34px;
    top: 96px;
  }
  .name {
    font-size: 30px;
    font-weight: 700;
    text-transform: uppercase;
    letter-spacing: 0.01em;
    line-height: 1;
  }
  .name .first { color: var(--gold); }
  .name .last { color: var(--white); }
  .title {
    margin-top: 8px;
    color: var(--white);
    font-size: 18px;
    letter-spacing: 0.02em;
  }
  .contact {
    margin-top: 20px;
    color: var(--white);
    font-size: 13px;
    line-height: 1.5;
    font-style: normal;
  }
  .disclaimer {
    position: absolute;
    left: calc(53% + 26px);
    right: 26px;
    top: 34px;
    color: var(--gold);
    font-size: 14.5px;
    line-height: 1.32;
  }
</style>
</head>
<body>
<main class="stage">
  <section class="card card-back" aria-label="Card back">
    <div class="brand">
      <span class="brand-dot"></span>
      <span class="brand-name">Brevik Partners</span>
    </div>
  </section>

  <section class="card card-front" aria-label="Card front">
    <div class="brand">
      <span class="brand-dot"></span>
      <span class="brand-name">Brevik Partners</span>
    </div>

    <div class="identity">
      <h1 class="name"><span class="first">Teodor</span> <span class="last">Brevik</span></h1>
      <p class="title">PRESIDENT</p>
      <address class="contact">
        Address is 4278<br>
        Pemberly Ave San Ramon<br>
        Ca. 94617<br>
        Phone: 510-647-3920<br>
        Fax: 925-413-7782<br>
        Email: teodor@brevikpartners.example
      </address>
    </div>

    <div class="divider"></div>

    <p class="disclaimer">
      Investment Advisor Representative of and Securities offered through
      Harwick Capital Brokerage, LLC Member NTVQA, OLBR and Registered
      Investment Advisor.
    </p>
  </section>
</main>
</body>
</html>
```